Brantley Fuel Retro Website Design

Have a logo. Need a website design to go along with the logo design. Full Design Specs are here: https://files.quorvand.net/doc/8QmXr2Lp-47tn806Hw3ZkYvB-Rs5cJ9aE/view

Target Market(s)

Independent Gas Station Owners

Number of Pages Required

1 page

Font styles to use
Sans Serif

Colors

Designer to choose colors to be used in the design.

```html
<!DOCTYPE html>
<html lang="en">
<head>
<meta charset="utf-8">
<title>Brantley Fuel</title>
<link rel="stylesheet" href="https://fonts.googleapis.com/css2?family=Lato:wght@400;700&family=Bebas+Neue&family=Roboto+Slab:wght@700&display=swap">
<style>
  :root {
    --red: #e8262b;
    --red-dark: #c81e22;
    --charcoal: #4b4b4b;
    --label: #555555;
    --page: #f6f6f6;
    --frame: #c9c9c9;
    --text: #333333;
    --white: #ffffff;
  }
  * { box-sizing: border-box; margin: 0; padding: 0; }
  html, body { width: 1200px; height: 2838px; overflow: hidden; background: var(--white); }
  body { font-family: "Lato", sans-serif; color: var(--text); position: relative; }
  .page { position: absolute; left: 187px; top: 7px; width: 822px; height: 2824px; background: var(--page); border: 1px solid var(--frame); }
  .abs { position: absolute; }

  .brand { left: 218px; top: 50px; display: flex; align-items: center; gap: 10px; }
  .brand-dot { width: 42px; height: 42px; border-radius: 50%; background: var(--red); }
  .brand-name { font-weight: 700; font-size: 19px; color: var(--charcoal); }
  .since { left: 782px; top: 44px; width: 220px; text-align: center; font-family: "Bebas Neue", sans-serif; color: var(--red); line-height: 1; }
  .since-year { font-size: 40px; }
  .since-phone { font-size: 23px; margin-top: 5px; }

  .nav { left: 201px; top: 138px; width: 795px; height: 53px; background: var(--red); border-radius: 6px; display: flex; align-items: center; padding-left: 12px; gap: 18px; }
  .nav a { color: var(--white); text-decoration: none; font-weight: 700; font-size: 12px; padding: 7px 10px; border-radius: 5px; }
  .nav a.is-active { background: var(--red-dark); }
  .nav a.is-hover { background: var(--charcoal); }

  .hero { left: 201px; top: 207px; width: 795px; height: 378px; border-radius: 6px; overflow: hidden;
    background:
      radial-gradient(ellipse 40% 25% at 62% 45%, rgba(220,215,210,0.55), transparent 70%),
      linear-gradient(180deg, #77797c 0%, #858789 30%, #b9b6b2 42%, #a8a29d 62%, #6a5650 70%, #4a4a4c 82%, #2f3033 100%); }
  .hero-disc { left: 269px; top: 259px; width: 222px; height: 222px; border-radius: 50%; background: rgba(70,70,72,0.82); }
  .hero-ribbon { left: 231px; top: 296px; width: 294px; height: 55px; }
  .hero-title { left: 231px; top: 296px; width: 294px; height: 55px; line-height: 55px; text-align: center; font-family: "Roboto Slab", serif; font-weight: 700; font-size: 29px; color: var(--white); }
  .hero-copy { left: 280px; top: 357px; width: 200px; text-align: center; font-size: 10.5px; line-height: 18px; color: var(--white); }

  .btn { display: block; background: var(--red); color: var(--white); text-align: center; font-size: 13px; text-decoration: none; border-radius: 3px; }
  .btn-hero { left: 325px; top: 407px; width: 108px; height: 27px; line-height: 27px; border-radius: 14px; font-size: 14px; }
  .btn-std { width: 90px; height: 29px; line-height: 29px; }

  .tag { background: var(--label); color: var(--white); font-weight: 700; font-size: 14px; text-align: center; border-radius: 4px; }
  .copy { font-size: 12px; line-height: 22.5px; }
  .copy-tight { font-size: 11.5px; line-height: 18px; }

  .fuel-photo { left: 200px; top: 631px; width: 374px; height: 336px; border-radius: 6px;
    background: linear-gradient(180deg, #c9d1d3 0%, #b9c2c5 40%, #8c8478 50%, #d9dbd9 58%, #c8cac8 75%, #4f5150 88%, #8a8e8c 100%); }
  .fuel-tag { left: 507px; top: 659px; width: 134px; height: 44px; line-height: 44px; }
  .fuel-copy { left: 641px; top: 762px; width: 340px; }
  .fuel-btn { left: 642px; top: 888px; }

  .oils-photo { left: 621px; top: 1012px; width: 374px; height: 337px; border-radius: 6px;
    background:
      radial-gradient(circle at 25% 30%, rgba(240,235,225,0.75), transparent 30%),
      radial-gradient(circle at 20% 88%, rgba(210,40,50,0.85), transparent 28%),
      radial-gradient(circle at 75% 80%, rgba(235,235,240,0.7), transparent 30%),
      linear-gradient(135deg, #9c7a52 0%, #6e5538 30%, #2a2a2e 55%, #3c3540 75%, #5a4a7a 100%); }
  .oils-tag { left: 579px; top: 1052px; width: 79px; height: 45px; line-height: 45px; }
  .oils-copy { left: 229px; top: 1158px; width: 340px; }
  .oils-btn { left: 229px; top: 1296px; }

  .carousel { left: 201px; top: 1397px; width: 795px; height: 260px;
    background:
      radial-gradient(ellipse 20% 30% at 90% 60%, rgba(160,50,50,0.35), transparent 70%),
      linear-gradient(90deg, #3a3430, #4a3f37 40%, #2f2c2c 70%, #2a2b33); }
  .slide { background:
      radial-gradient(circle at 80% 70%, rgba(230,230,235,0.6), transparent 30%),
      linear-gradient(180deg, #8c6f52 0%, #2f3f6e 40%, #8a6a4e 65%, #b5453c 100%); }
  .slide-a { left: 279px; top: 1459px; width: 166px; height: 125px; }
  .slide-b { left: 500px; top: 1443px; width: 208px; height: 156px; }
  .slide-c { left: 763px; top: 1459px; width: 166px; height: 125px; }
  .arrow { top: 1500px; width: 30px; height: 44px; }

  .farm-main { left: 200px; top: 1705px; width: 262px; height: 224px;
    background: linear-gradient(180deg, #7a6e62 0%, #8d8882 18%, #9ea1a4 35%, #7f8286 70%, #6a6c6e 82%, #a59a88 100%); }
  .farm-title { left: 529px; top: 1726px; width: 400px; text-align: center; font-weight: 700; font-size: 14px; }
  .farm-copy { left: 519px; top: 1766px; width: 420px; text-align: center; }
  .farm-btn { left: 687px; top: 1845px; }
  .tank { top: 1936px; width: 262px; height: 224px;
    background: linear-gradient(180deg, #6f6a64 0%, #8e8a84 18%, #eeeeee 38%, #e2e2e2 65%, #c4c4c4 80%, #8b867e 100%); }
  .tank-a { left: 200px; }
  .tank-b { left: 467px; }
  .tank-c { left: 734px; background: linear-gradient(180deg, #5e5a54 0%, #8a8680 45%, #e8e8e8 58%, #d6d6d6 80%, #9a958c 100%); }

  .cargo-a { left: 224px; top: 2218px; width: 299px; height: 272px;
    background: linear-gradient(90deg, #7e8286 0%, #8e9296 45%, #6e7378 78%, #9b968a 100%); }
  .cargo-b { left: 408px; top: 2424px; width: 263px; height: 212px; border: 2px solid #e2e2e2;
    background: linear-gradient(180deg, #d0d3d6 0%, #bfc3c6 30%, #8d9297 50%, #7a7f84 70%, #6f7a5f 85%, #5d6650 100%); }
  .cargo-tag { left: 451px; top: 2239px; width: 157px; height: 43px; line-height: 43px; }
  .cargo-copy { left: 579px; top: 2299px; width: 380px; }
  .cargo-btn { left: 579px; top: 2368px; }

  .footer { left: 200px; top: 2691px; width: 797px; height: 125px; background: var(--charcoal); border-top: 4px solid var(--red); }
  .footer-brand { left: 250px; top: 2722px; display: flex; align-items: center; gap: 8px; }
  .footer-dot { width: 36px; height: 36px; border-radius: 50%; background: var(--red); }
  .footer-name { font-weight: 700; font-size: 14px; color: var(--white); }
  .footer-copy { left: 237px; top: 2790px; font-size: 10.5px; color: var(--white); }
</style>
</head>
<body>
  <div class="page"></div>

  <header>
    <div class="abs brand"><span class="brand-dot"></span><span class="brand-name">Brantley Fuel</span></div>
    <div class="abs since">
      <div class="since-year">SINCE 1996</div>
      <div class="since-phone">PHONE : 5550142276</div>
    </div>
    <nav class="abs nav">
      <a href="#" class="is-active">HOME</a>
      <a href="#" class="is-hover">FUEL DELIEVERY</a>
      <a href="#">OIL</a>
      <a href="#">FARM FUEL</a>
      <a href="#">CARGO CONTAINERS</a>
    </nav>
  </header>

  <section>
    <div class="abs hero" role="img" aria-label="Photo of the Brantley Fuel shop building with trucks parked out front"></div>
    <div class="abs hero-disc"></div>
    <svg class="abs hero-ribbon" viewBox="0 0 294 55" aria-hidden="true">
      <polygon points="0,0 294,0 270,27.5 294,55 0,55 24,27.5" fill="#e8262b"/>
    </svg>
    <h1 class="abs hero-title">WE ARE HERE</h1>
    <p class="abs hero-copy">Fuel Delivery , Oil delivery ,Brantley Fuel has been around since 1966</p>
    <a href="#" class="abs btn btn-hero">More</a>
  </section>

  <section>
    <div class="abs fuel-photo" role="img" aria-label="Photo of a white fuel delivery truck under a cloudy sky"></div>
    <h2 class="abs tag fuel-tag">FUEL DELIVERY</h2>
    <p class="abs copy fuel-copy">Brantley Fuel provides fuel delivery for independent gas stations, convenience stores, construction sites or any other commercial need. If you are looking for gasoline, high sulfer diesel fuel, farm diesel or other bulk fuel delivered to your business, we will take care of you!</p>
    <a href="#" class="abs btn btn-std fuel-btn">More</a>
  </section>

  <section>
    <div class="abs oils-photo" role="img" aria-label="Photo of motor oil jugs and price signs on store shelves"></div>
    <h2 class="abs tag oils-tag">OILS</h2>
    <p class="abs copy oils-copy">Looking for speciality auto, tractor, tractor trailer, aviation or other commercial oils and lubricants Brantley Fuel can help! Just call one of our customer oriented staff and we will get what you need quick! We have a complete line of aviation oils and lubricants as well as gear lubricants, greases, oils and more!</p>
    <a href="#" class="abs btn btn-std oils-btn">More</a>
  </section>

  <section>
    <div class="abs carousel" role="img" aria-label="Blurred photo of the store interior behind the gallery"></div>
    <div class="abs slide slide-a" role="img" aria-label="Photo of store shelves stocked with supplies"></div>
    <div class="abs slide slide-b" role="img" aria-label="Photo of shelves full of oil bottles"></div>
    <div class="abs slide slide-c" role="img" aria-label="Photo of oil products on display by a window"></div>
    <svg class="abs arrow" style="left:210px" viewBox="0 0 30 44" aria-hidden="true"><polyline points="26,2 4,22 26,42" fill="none" stroke="#fff" stroke-width="2.5"/></svg>
    <svg class="abs arrow" style="left:955px" viewBox="0 0 30 44" aria-hidden="true"><polyline points="4,2 26,22 4,42" fill="none" stroke="#fff" stroke-width="2.5"/></svg>
  </section>

  <section>
    <div class="abs farm-main" role="img" aria-label="Photo of a large gray fuel storage tank"></div>
    <h2 class="abs farm-title">FARM FUEL</h2>
    <p class="abs copy-tight farm-copy">Looking for gasoline, diesel red diesel off road fuel or farm diesel? We can deliver straight to your farm! We can setup your farm tanks, take care of EPA containment and deliver fuel when you need it!</p>
    <a href="#" class="abs btn btn-std farm-btn">More</a>
    <div class="abs tank tank-a" role="img" aria-label="Photo of two white farm fuel tanks"></div>
    <div class="abs tank tank-b" role="img" aria-label="Photo of a white fuel tank on gravel"></div>
    <div class="abs tank tank-c" role="img" aria-label="Photo of a white fuel tank by bare trees"></div>
  </section>

  <section>
    <div class="abs cargo-a" role="img" aria-label="Photo of the doors of a gray cargo container"></div>
    <div class="abs cargo-b" role="img" aria-label="Photo of a gray cargo container on grass"></div>
    <h2 class="abs tag cargo-tag">CARGO CONTAINERS</h2>
    <p class="abs copy-tight cargo-copy">Want to purchase or lease a storage container, we have what you need! We can deliver or move storage containers to your home, business, construction site or any you need one!</p>
    <a href="#" class="abs btn btn-std cargo-btn">More</a>
  </section>

  <footer>
    <div class="abs footer"></div>
    <div class="abs footer-brand"><span class="footer-dot"></span><span class="footer-name">Brantley Fuel</span></div>
    <p class="abs footer-copy">© 2019brantleyfuel.com</p>
  </footer>
</body>
</html>
```